Larkmoor Capital Partners need a desert themed website!

We need a web design and development for our informational website for our new company named Larkmoor Capital Partners. We would like it to be desert themed and it can be color or black and white. We would like it to be classy and clean, while also talking to the benefits of investment partner with us.

We're thinking probably a home page with a nice image of a Larkmoor landscape, then other pages would What we offer our partners page (or other wording if you find something better), a meet the founder page, and a contact us page.

What we offer our partners (or other wording if you think of something better):
Our investors offer an opportunity to families that cannot usually get approved for a mortgage, to be able to become future homeowners. Thus, Benefiting both the investors and local surrounding community members. Our investors get to both have all the benefits of an investment with receiving above market rates of return to themselves and helping families find homes at the same time.

Maybe also build an infographic with these benefits: Safety, Security, Long-term investment horizon, cashflow, tax benefits, above market rate of return, and capital growth.

And a meet the founder page. With my headshot.

Dale Corwith is a private equity investor providing significantly above market returns to his investment partners while taking the time to be involved with his community and family. Dale first honed his skills in taking calculated risk decisions while very young where he took on playing poker professionally. He succeeded at the highest levels for over a decade competing in high stakes professional cash games around the world.

From the poker world he transitioned to investing in public and private markets. He took an approach of knowing the companies he invests in intimately and after over 10,000 hours of research became known in his community as the person to get investment advice on the electric vehicle industry for his voracious research and expert insight.

He now invests in single family homes in the Phoenix market using his past experience analyzing probabilistic outcomes and comparing the ROIs of different potential strategies. These skills have contributed to his success in investing in companies where he used his ability to assess risk to reward ratios to significantly outperform the market over an extended period.

Contact page we want my email Dale@LarkmoorFunds.example, my instagram: @DaleCorwith, and my linkedin https://www.profilehub.example/in/dale-corwith-58172036/

I have included my headshot for the about me page. I've included some saguaro generated images feel free to incorporate into the website (or make them the company logo), or not, whatever you feel gives the best look for the website.

```html
<!DOCTYPE html>
<html lang="en">
<head>
<meta charset="utf-8">
<title>Larkmoor Capital Partners</title>
<link href="https://fonts.googleapis.com/css2?family=Montserrat:wght@400;500;600;700;800&family=Poppins:wght@400;500;600&family=Jost:wght@500;600&display=swap" rel="stylesheet">
<style>
:root{
  --ink:#1f1f1f;
  --dark:#2b2b2b;
  --panel:#262626;
  --field:#5a5a5a;
  --white:#ffffff;
  --muted:#555555;
  --line:#d8d8d8;
  --dot:#c9c9c9;
  --sand:#8a6238;
  --sky:#4a4d52;
}
*{box-sizing:border-box;margin:0;padding:0}
html,body{width:1200px;height:3392px;overflow:hidden;background:var(--white)}
body{position:relative;font-family:"Poppins",sans-serif;color:var(--ink)}
.abs{position:absolute}

/* hero */
.hero{left:0;top:0;width:1200px;height:667px;
  background:linear-gradient(180deg,#3d4a5c 0%,#6f7c8a 22%,#a08468 42%,#6b4a2c 62%,#3a2818 100%)}
.hero-shade{left:0;top:0;width:1200px;height:667px;background:linear-gradient(180deg,rgba(0,0,0,.25),rgba(0,0,0,.05) 40%,rgba(0,0,0,.35))}
.brand{left:122px;top:32px;width:90px;text-align:center;color:var(--white);font-family:"Montserrat",sans-serif;font-weight:700;font-size:10px;line-height:1.15}
.brand .mark{display:block;width:40px;height:40px;border-radius:50%;background:#d9b48a;margin:0 auto 4px}
.nav{left:386px;top:46px;display:flex;gap:52px;font-size:13px;color:var(--white)}
.btn-details{left:965px;top:40px;width:108px;height:30px;border-radius:15px;background:var(--white);color:var(--ink);font-size:10px;font-weight:600;display:flex;align-items:center;justify-content:center}
.hero-title{left:0;top:318px;width:1200px;text-align:center;color:var(--white);font-family:"Montserrat",sans-serif;font-weight:800;font-size:76px;letter-spacing:2px;line-height:1}
.hero-sub{left:0;top:414px;width:1200px;text-align:center;color:var(--white);font-family:"Montserrat",sans-serif;font-weight:700;font-size:38px;letter-spacing:1px}
.hero-text{left:322px;top:476px;width:556px;text-align:center;color:#eee;font-size:12.5px;line-height:1.55}
.btn-light{left:520px;top:578px;width:138px;height:36px;border-radius:18px;background:var(--white);color:var(--ink);font-size:11px;font-weight:600;display:flex;align-items:center;justify-content:center}

/* about */
.portrait{left:125px;top:770px;width:448px;height:594px;background:linear-gradient(160deg,#6a5a4c,#8c7867 45%,#5d5650 100%)}
.about-title{left:661px;top:880px;font-family:"Montserrat",sans-serif;font-weight:800;font-size:66px;letter-spacing:2px;line-height:1}
.about-sub{left:661px;top:958px;font-family:"Montserrat",sans-serif;font-weight:700;font-size:26px}
.about-text{left:661px;top:1007px;width:500px;font-size:12.5px;line-height:1.65;color:var(--muted)}
.btn-dark{left:661px;top:1194px;width:138px;height:40px;border-radius:20px;background:var(--dark);color:var(--white);font-size:11px;font-weight:600;display:flex;align-items:center;justify-content:center}

/* benefits */
.benefits{left:0;top:1472px;width:1200px;height:778px;
  background:linear-gradient(180deg,#ffffff 0%,#8a8c8f 14%,#55585c 38%,#6e6660 52%,#9a7048 66%,#6b4828 84%,#3c2616 100%)}
.ben-title{left:0;top:1982px;width:1200px;text-align:center;color:var(--white);font-family:"Montserrat",sans-serif;font-weight:800;font-size:72px;letter-spacing:3px;line-height:1}
.ben-sub{left:0;top:2054px;width:1200px;text-align:center;color:var(--white);font-family:"Montserrat",sans-serif;font-weight:700;font-size:38px}
.ben-text{left:300px;top:2122px;width:600px;text-align:center;color:#eee;font-size:12.5px;line-height:1.65}
.card{top:2300px;width:238px;height:206px;background:var(--white);box-shadow:0 6px 24px rgba(0,0,0,.12);text-align:center}
.card svg{margin-top:30px}
.card h3{font-family:"Montserrat",sans-serif;font-weight:700;font-size:24px;margin-top:14px}
.card .more{display:inline-block;margin-top:10px;font-size:12px;font-weight:600;border-bottom:2px solid var(--ink);padding-bottom:2px}
.dots{left:493px;top:2555px;display:flex;gap:22px}
.dots span{width:12px;height:12px;border-radius:50%;background:var(--dot)}
.dots span.on{background:var(--ink)}

/* contact */
.contact-bg{left:0;top:2930px;width:1200px;height:404px;background:linear-gradient(180deg,#b7aea5,#c9a98a 45%,#9c8a74 75%,#6e6a5e)}
.contact-panel{left:125px;top:2672px;width:950px;height:320px;background:var(--panel)}
.contact-title{left:215px;top:2732px;font-family:"Jost",sans-serif;font-weight:600;font-size:48px;color:var(--white)}
.contact-list{left:213px;top:2813px;list-style:none;color:var(--white);font-size:13px}
.contact-list li{display:flex;align-items:center;gap:26px;height:42px}
.contact-list .ic{width:30px;height:30px;border-radius:50%;background:#e6e6e6;display:flex;align-items:center;justify-content:center}
.field{background:var(--field);color:#e8e8e8;font-size:12px;padding:12px 16px}
.f-name{left:536px;top:2718px;width:222px;height:46px}
.f-email{left:772px;top:2718px;width:216px;height:46px}
.f-subject{left:536px;top:2778px;width:452px;height:46px}
.f-msg{left:536px;top:2838px;width:452px;height:108px}

/* footer */
.foot-brand{left:450px;top:3080px;width:300px;text-align:center;font-family:"Montserrat",sans-serif;font-weight:700;font-size:22px;color:var(--ink);line-height:1.1}
.foot-brand .mark{display:block;width:58px;height:58px;border-radius:50%;background:#c98f5c;margin:0 auto 8px}
.social{left:560px;top:3212px;display:flex;gap:16px}
.social span{width:32px;height:32px;border-radius:50%;border:2px solid var(--ink);background:rgba(255,255,255,.3)}
.foot-nav{left:398px;top:3282px;display:flex;gap:80px;font-size:11px;font-weight:500;color:var(--ink)}
.copy{left:0;top:3334px;width:1200px;height:58px;background:var(--dark);color:var(--white);font-size:11px;display:flex;align-items:center;justify-content:center;letter-spacing:.5px}
</style>
</head>
<body>

<header>
  <div class="abs hero" role="img" aria-label="Desert landscape with saguaro and cholla cacti at sunset"></div>
  <div class="abs hero-shade"></div>
  <div class="abs brand"><span class="mark"></span>LARKMOOR CAPITAL PARTNERS</div>
  <nav class="abs nav"><span>Home</span><span>What We Offer</span><span>A Meet The Founder</span><span>Contact</span></nav>
  <div class="abs btn-details">Get Details</div>
  <h1 class="abs hero-title">LARKMOOR</h1>
  <p class="abs hero-sub">CAPITAL PARTNERS</p>
  <p class="abs hero-text">Lorem Ipsum is simply dummy text of the printing and typesetting industry. Lorem Ipsum has been the industry's standard dummy text ever since the 1500s, when an unknown printer took a galley of type and scrambled it to...</p>
  <div class="abs btn-light">Read More</div>
</header>

<section class="about">
  <div class="abs portrait" role="img" aria-label="Headshot of founder Dale Corwith"></div>
  <h2 class="abs about-title">ABOUT US</h2>
  <p class="abs about-sub">Investing In Your Success</p>
  <p class="abs about-text">Dale Corwith is a private equity investor providing significantly above market returns to his investment partners while taking the time to be involved with his community and family. Dale first honed his skills in taking calculated risk decisions while very young where he took on playing poker professionally. He succeeded at the highest levels for over a decade competing in high stakes professional cash games around the world.</p>
  <div class="abs btn-dark">Read More</div>
</section>

<section class="benefit-section">
  <div class="abs benefits" role="img" aria-label="Desert sand dunes under a cloudy grey sky"></div>
  <h2 class="abs ben-title">BENIFITS</h2>
  <p class="abs ben-sub">Where Benefits Meet Your Needs</p>
  <p class="abs ben-text">Our investors offer an opportunity to families that cannot usually get approved for a mortgage, to be able to become future homeowners. Thus, Benefiting both the investors and local surrounding community members. Our investors get to both have all the benefits of an investment with receiving above market rates of return to themselves and helping families find homes at the same time.</p>

  <div class="abs card" style="left:64px">
    <svg width="44" height="48" viewBox="0 0 44 48"><path d="M22 2 L40 9 V22 C40 34 32 42 22 46 C12 42 4 34 4 22 V9 Z" fill="#1f1f1f"/><path d="M22 14 V32 M13 23 H31" stroke="#fff" stroke-width="5"/></svg>
    <h3>Safety</h3><span class="more">READ MORE</span>
  </div>
  <div class="abs card" style="left:342px">
    <svg width="44" height="48" viewBox="0 0 44 48"><path d="M22 2 L40 9 V22 C40 34 32 42 22 46 C12 42 4 34 4 22 V9 Z" fill="none" stroke="#1f1f1f" stroke-width="3"/><rect x="14" y="21" width="16" height="13" rx="2" fill="#1f1f1f"/><path d="M17 21 V17 a5 5 0 0 1 10 0 V21" fill="none" stroke="#1f1f1f" stroke-width="3"/></svg>
    <h3>Security</h3><span class="more">READ MORE</span>
  </div>
  <div class="abs card" style="left:620px">
    <svg width="48" height="48" viewBox="0 0 48 48"><path d="M8 16 A18 18 0 0 1 40 14" fill="none" stroke="#1f1f1f" stroke-width="3"/><path d="M40 32 A18 18 0 0 1 8 34" fill="none" stroke="#1f1f1f" stroke-width="3"/><path d="M36 8 L41 15 L33 16 Z M12 40 L7 33 L15 32 Z" fill="#1f1f1f"/><circle cx="24" cy="24" r="11" fill="#1f1f1f"/><text x="24" y="29" text-anchor="middle" font-family="Montserrat,sans-serif" font-weight="700" font-size="14" fill="#fff">$</text></svg>
    <h3>Cashflow</h3><span class="more">READ MORE</span>
  </div>
  <div class="abs card" style="left:895px">
    <svg width="44" height="50" viewBox="0 0 44 50"><rect x="6" y="4" width="32" height="14" fill="none" stroke="#1f1f1f" stroke-width="3"/><text x="22" y="15" text-anchor="middle" font-family="Montserrat,sans-serif" font-weight="700" font-size="9" fill="#1f1f1f">TAX</text><path d="M22 18 V46 M14 26 H30 M14 34 H30" stroke="#1f1f1f" stroke-width="3"/></svg>
    <h3>Tax Benefits</h3><span class="more">READ MORE</span>
  </div>

  <div class="abs dots"><span></span><span></span><span></span><span class="on"></span><span></span><span></span><span></span></div>
</section>

<section class="contact">
  <div class="abs contact-bg" role="img" aria-label="Soft-focus desert landscape with cacti"></div>
  <div class="abs contact-panel"></div>
  <h2 class="abs contact-title">Contact Us</h2>
  <ul class="abs contact-list">
    <li><span class="ic"><svg width="14" height="10" viewBox="0 0 14 10"><rect x=".5" y=".5" width="13" height="9" fill="none" stroke="#262626"/><path d="M.5 .5 L7 6 L13.5 .5" fill="none" stroke="#262626"/></svg></span>Dale@LarkmoorFunds.example</li>
    <li><span class="ic"></span>@DaleCorwith</li>
    <li><span class="ic"></span>Larkmoor Capital Partners</li>
  </ul>
  <div class="abs field f-name">Name</div>
  <div class="abs field f-email">Email</div>
  <div class="abs field f-subject">Subject</div>
  <div class="abs field f-msg">Message</div>
</section>

<footer>
  <div class="abs foot-brand"><span class="mark"></span>LARKMOOR CAPITAL PARTNERS</div>
  <div class="abs social"><span></span><span></span></div>
  <nav class="abs foot-nav"><span>HOME</span><span>BENIFITS</span><span>WHAT WE OFFER</span><span>CONTACT US</span></nav>
  <div class="abs copy">COPYRIGHT©2023 LARKMOOR ALL RIGHTS RESERVED</div>
</footer>

</body>
</html>
```